Vimo wine label

Get all the info (Picture of another bottle & Logo) on a label on a thin wrap label, label size 1.5" width and 11-12" length. Also need Wine Name "VIMO" and grape varietal "Gamay" and "Alc. By Vol. 12.8%"

```html
<!DOCTYPE html>
<html lang="en">
<head>
<meta charset="utf-8">
<title>Vimo wine label</title>
<link rel="stylesheet" href="https://fonts.googleapis.com/css2?family=Cinzel:wght@400;500&display=swap">
<style>
  :root {
    --page-bg: #efeae2;
    --label-dark: #1c1c1c;
    --label-mid: #3a3a3a;
    --gold: #d2a03a;
    --gold-line: #c9973a;
    --ivory: #f4f1ea;
  }
  * { margin: 0; padding: 0; box-sizing: border-box; }
  html, body {
    width: 1200px;
    height: 331px;
    overflow: hidden;
    background: var(--page-bg);
  }
  .wrap-label {
    position: absolute;
    left: 30px;
    top: 94px;
    width: 1140px;
    height: 143px;
    overflow: hidden;
    background:
      radial-gradient(ellipse at 50% 45%, var(--label-mid) 0%, #2a2a2a 45%, var(--label-dark) 100%);
  }
  .label-frame {
    position: absolute;
    left: 10px;
    top: 11px;
    right: 10px;
    bottom: 10px;
    border: 1.5px solid var(--gold-line);
  }
  .label-row {
    position: absolute;
    top: 0;
    height: 143px;
    display: flex;
    align-items: center;
    white-space: nowrap;
    font-family: "Cinzel", "Times New Roman", serif;
  }
  .label-row--first { left: 32px; }
  .label-row--second { left: 583px; }
  .wine-name {
    display: block;
    width: 164px;
    margin-right: 6px;
    font-size: 54px;
    font-weight: 400;
    color: var(--gold);
    letter-spacing: 1px;
    line-height: 1;
    padding-top: 8px;
  }
  .varietal,
  .abv {
    font-size: 19px;
    font-weight: 400;
    color: var(--ivory);
    letter-spacing: 0.3px;
    line-height: 1;
  }
  .divider {
    width: 2px;
    height: 26px;
    background: var(--gold);
    margin: 0 10px 0 8px;
  }
</style>
</head>
<body>
  <div class="wrap-label" role="img" aria-label="Dark charcoal label with a subtle damask pattern">
    <div class="label-frame"></div>

    <div class="label-row label-row--first">
      <span class="wine-name">VIMO</span>
      <span class="varietal">GRAPE VARIETAL</span>
      <span class="divider"></span>
      <span class="abv">Alc. By Vol. 12.8%</span>
    </div>

    <div class="label-row label-row--second">
      <span class="wine-name">VIMO</span>
      <span class="varietal">GRAPE VARIETAL</span>
      <span class="divider"></span>
      <span class="abv">Alc. By Vol. 12.8%</span>
    </div>
  </div>
</body>
</html>
```